Web Design for Small Healthcare Startup

Hello,

We are seeking a Website Design for a healthcare company focusing on mobile vaccinations, employee health and wellness services onsite at businesses, and consulting services relating to Healthcare Entities in WA state. Our company’s mission is to “To aid in a healthier workplace”. Brightpath Rovers will provide on-site wellness services to employers that simplify and streamline employee preventative health as well as onsite consulting services to help with compliance of Healthcare Entities.

We are seeking a Website Design for Brightpath Rovers, PLLC. Our company’s mission is to provide mobile health and wellness services to employers onsite at their businesses. These services include mobile vaccinations clinics for employees as well as wellness and health screenings. The company will also offer healtcare compliance consulting services for Healthcare Entities. The company was founded to bring these important healthcare services to businesses and keep employees healthy. Healthy employees are the cornerstone to a great business and we want to help orginazations achieve their goals of having a healthy productive workforce.

We are looking for a moderin website design that will need to be coded. We have attached our current logo design for reference as well as a brief questionare regarding our business for your information (not necessary to include all information). We would like something SEO friendly and easy to navigate.

Thank you!

Brightpath Rovers, PLLC

Target Market(s)

Small Businesses

Industry/Entity Type

Healthcare

Coding

Coded - Design and coding required

Number of Pages Required

1 page

Requirements
Nice to have
• SEO Friendly, Incorporate Logo

```html
<!DOCTYPE html>
<html lang="en">
<head>
<meta charset="utf-8">
<title>Brightpath Rovers, PLLC — Mobile Vaccine Clinics</title>
<link href="https://fonts.googleapis.com/css2?family=Roboto:wght@300;400;500;700;900&display=swap" rel="stylesheet">
<style>
:root{
  --purple:#9b3f98;
  --purple-dark:#6b3d99;
  --navy:#1b2563;
  --blue:#0450a8;
  --blue-link:#1d5bbf;
  --ink:#1d1d2b;
  --muted:#6d6d78;
  --page:#eef2fa;
  --topbar:#f5f7fb;
  --footer:#efefef;
  --teal:#2ccaa8;
  --pink:#d9aad5;
  --sky:#0a8cc8;
  --steel:#2a5f93;
}
*{box-sizing:border-box;margin:0;padding:0}
html,body{width:772px;height:1200px;overflow:hidden}
body{font-family:'Roboto',Arial,sans-serif;color:var(--ink);background:#fff;position:relative}
.abs{position:absolute}
a{color:inherit;text-decoration:none}

.topbar{left:0;top:0;width:772px;height:17px;background:var(--topbar);font-size:6px;color:var(--ink)}
.topbar .welcome{left:120px;top:5px}
.topbar .welcome span,.topbar .help span{color:var(--purple)}
.topbar .help{left:486px;top:5px;display:flex;gap:3px;align-items:center}
.social{display:flex;gap:7px}
.social i{display:block;width:6px;height:6px;border-radius:50%;background:var(--blue-link)}
.topbar .social{left:614px;top:6px}

.header{left:0;top:17px;width:772px;height:43px;background:#fff}
.brand{display:flex;align-items:center;gap:4px;font-weight:700;color:var(--blue-link);font-size:11px}
.brand i{display:block;width:10px;height:10px;border-radius:50%;background:var(--purple)}
.header .brand{left:120px;top:15px}
.nav{left:361px;top:18px;display:flex;gap:16px;font-size:7px;font-weight:500}
.nav .active{color:var(--purple);position:relative}
.nav .active::after{content:"";position:absolute;left:0;right:0;top:18px;height:2px;background:var(--purple)}
.btn-appt{left:580px;top:11px;width:70px;height:20px;background:var(--purple);color:#fff;font-size:7px;font-weight:500;border-radius:2px;display:flex;align-items:center;justify-content:center;gap:4px}

.hero{left:0;top:60px;width:772px;height:220px;background:linear-gradient(100deg,#15205a 0%,#1e2f78 55%,#2d4090 100%);overflow:hidden}
.hero-photo{left:400px;top:0;width:290px;height:220px;background:radial-gradient(ellipse at 55% 55%,#e6e9f2 0%,#b9c2da 45%,rgba(45,64,144,0) 75%)}
.hero h1{left:120px;top:60px;font-size:26px;line-height:30px;font-weight:700;color:#fff}
.hero h1 span{background:linear-gradient(transparent 62%,var(--purple) 62%,var(--purple) 92%,transparent 92%)}
.hero p{left:120px;top:127px;width:220px;font-size:8px;line-height:12px;color:#fff;font-weight:300}
.arrow{width:17px;height:17px;border-radius:50%;background:var(--blue-link);display:flex;align-items:center;justify-content:center}
.arrow.prev{left:91px;top:102px}
.arrow.next{left:663px;top:102px}

.features{left:0;top:280px;width:772px;height:265px;background:var(--page)}
.card{top:9px;width:127px;height:177px;color:#fff;padding:0 12px;display:flex;flex-direction:column;justify-content:center;font-size:11.5px;line-height:13.5px;font-weight:300}
.card b{font-weight:700}
.card.c1{left:120px;background:linear-gradient(160deg,#2fd2ad,#27c2a4);padding-bottom:36px}
.card.c2{left:257px;background:linear-gradient(160deg,#dcb1d8,#cf9ecb);color:var(--ink);font-size:16px;line-height:17px;font-weight:400;justify-content:flex-start;padding-top:33px}
.card.c3{left:393px;background:linear-gradient(160deg,#0a95cf,#0a7fbf);padding-top:50px}
.card.c4{left:529px;background:linear-gradient(180deg,#2a63a2,#2c5878);font-size:16px;line-height:17.5px;font-weight:400;justify-content:flex-start;padding-top:40px;padding-left:15px}
.reserve{left:0;top:211px;width:772px;text-align:center;font-size:11px}

.steps{left:0;top:545px;width:772px;height:284px;background:#fff}
.steps-photo{left:0;top:0;width:353px;height:284px;background:linear-gradient(120deg,#e9edf1 0%,#cfd6de 50%,#a9b3bf 100%)}
.step{left:352px;display:flex;align-items:center;gap:6px;width:300px;height:46px;background:linear-gradient(90deg,rgba(240,240,244,0) 0%,#f1f1f4 50%,rgba(240,240,244,0) 100%)}
.step .num{width:39px;height:39px;border-radius:50%;background:linear-gradient(135deg,#a24b9c,#5a4aa8);color:#fff;display:flex;flex-direction:column;align-items:center;justify-content:center;font-size:6px;line-height:7px}
.step .num b{font-size:20px;line-height:20px;font-weight:900}
.step p{font-size:12px;line-height:15px;font-weight:300}
.s1{top:36px}.s2{top:82px}.s3{top:129px}
.callbox{left:353px;top:176px;width:419px;height:108px;background:var(--blue);color:#fff;padding:15px 17px}
.callbox .lead{font-size:10.5px;font-weight:300}
.callbox .phone{font-size:14px;font-weight:700;margin-top:2px}
.btn-cal{margin-top:9px;width:103px;height:28px;border:1px solid #fff;display:flex;align-items:center;justify-content:center;gap:6px;font-size:8px;font-weight:500}

.about{left:0;top:829px;width:772px;height:253px;background:linear-gradient(110deg,#a6439a 0%,#8a4aa2 45%,#4c52a9 100%);color:#fff;text-align:center}
.about .eyebrow{margin-top:51px;font-size:7px}
.about .sub{font-size:6.5px;font-weight:700;margin-top:4px}
.about h2{font-size:16px;font-weight:700;margin-top:7px}
.about .rule{width:17px;height:2px;background:#fff;margin:13px auto 0}
.about p{width:465px;margin:16px auto 0;font-size:7px;line-height:11px;font-weight:300}
.btn-more{display:inline-flex;margin-top:17px;width:71px;height:20px;background:var(--navy);align-items:center;justify-content:center;font-size:7px;font-weight:500;border-radius:2px}

.footer{left:0;top:1082px;width:772px;height:118px;background:var(--footer)}
.footer .brand{position:absolute;left:0;width:772px;justify-content:center;top:36px}
.fnav{left:120px;top:68px;width:531px;height:16px;border-top:1px solid #d6d6d6;border-bottom:1px solid #d6d6d6;display:flex;justify-content:center;align-items:center;font-size:7px;font-weight:500;color:var(--navy)}
.fnav span.sep{color:#aaa;margin:0 7px}
.copy{left:120px;top:91px;font-size:6.5px;color:var(--muted)}
.copy span{color:var(--blue-link)}
.footer .social{left:616px;top:93px}
</style>
</head>
<body>

<div class="abs topbar">
  <div class="abs welcome">Welcome to <span>Brightpath Rovers Pllc</span></div>
  <div class="abs help">
    <svg width="7" height="7" viewBox="0 0 24 24" fill="none" stroke="#1d5bbf" stroke-width="2"><path d="M5 3h4l2 5-3 2a12 12 0 0 0 6 6l2-3 5 2v4a2 2 0 0 1-2 2A18 18 0 0 1 3 5a2 2 0 0 1 2-2z"/></svg>
    Emergancy Helpline: <span>555-014-7290</span>
  </div>
  <div class="abs social"><i></i><i></i><i></i></div>
</div>

<header class="abs header">
  <div class="abs brand"><i></i>Brightpath Rovers</div>
  <nav class="abs nav">
    <a class="active">Home</a><a>Aboute</a><a>Services</a><a>Schedule Today</a><a>Pricing</a>
  </nav>
  <a class="abs btn-appt">
    <svg width="8" height="8" viewBox="0 0 24 24" fill="none" stroke="#fff" stroke-width="2"><rect x="3" y="5" width="18" height="16" rx="1"/><path d="M3 10h18M8 3v4M16 3v4M9 15l2 2 4-4"/></svg>
    Appointment
  </a>
</header>

<section class="abs hero">
  <div class="abs hero-photo" role="img" aria-label="Lab worker in protective suit holding a blood sample and a vaccine vial"></div>
  <h1 class="abs"><span>Making The Workplace</span><br><span>a Healthier Place.</span></h1>
  <p class="abs">Be clean &amp; Keep Cklean, Maintaing Social Distance, Avoid All Kinds of Crowds including Social Gathering, Protect Yourself and Others, Save Humankind!</p>
  <div class="abs arrow prev"><svg width="6" height="6" viewBox="0 0 10 10"><path d="M6.5 1.5 3 5l3.5 3.5" fill="none" stroke="#fff" stroke-width="1.2"/></svg></div>
  <div class="abs arrow next"><svg width="6" height="6" viewBox="0 0 10 10"><path d="M3.5 1.5 7 5 3.5 8.5" fill="none" stroke="#fff" stroke-width="1.2"/></svg></div>
</section>

<section class="abs features">
  <div class="abs card c1"><b>Brightpath Rovers specializes in</b> providing seamless, hassle-free, on-site mobile vaccine clinics.</div>
  <div class="abs card c2">No crowded waiting rooms, no long lines, no hassle!</div>
  <div class="abs card c3"><b>Specializing in</b> Workplace employee vaccine clinics. Great service to offer as part of your company’s Employee Wellness Package.</div>
  <div class="abs card c4">Offering Flu and Covid vaccinations</div>
  <div class="abs reserve">Reserve Your On-Site MobileVaccine Clinic Today!</div>
</section>

<section class="abs steps">
  <div class="abs steps-photo" role="img" aria-label="Man at a laptop filling in the clinic questionnaire"></div>
  <div class="abs step s1"><div class="num">STEPS<b>1</b></div><p>Submit Vaccine Clinic Needs<br>Questionnaire.</p></div>
  <div class="abs step s2"><div class="num">STEPS<b>2</b></div><p>Brightpath Rovers, PLLC will contact<br>you to schedule on-site vaccine clinic.</p></div>
  <div class="abs step s3"><div class="num">STEPS<b>3</b></div><p>Prepare your employees for vaccine<br>clinic day.</p></div>
  <div class="abs callbox">
    <div class="lead">Or Call Directly For More Information</div>
    <div class="phone">555-014-7290</div>
    <a class="btn-cal">
      <svg width="14" height="13" viewBox="0 0 24 22" fill="none" stroke="#fff" stroke-width="1.3"><rect x="1" y="3" width="17" height="15"/><path d="M1 7h17M5 1v4M14 1v4M4 10h2M8 10h2M12 10h2M4 13h2M8 13h2"/><circle cx="18" cy="16" r="5" fill="#0450a8"/><path d="M18 13.5V16l1.5 1.5"/></svg>
      Calendar
    </a>
  </div>
</section>

<section class="abs about">
  <div class="eyebrow">ABOUT</div>
  <div class="sub">BRIGHTPATH ROVERS, PLLC MISSION</div>
  <h2>Making The Workplace A Healthier Place</h2>
  <div class="rule"></div>
  <p>To provide on-sitewellness services to employers that simplify and streamline employee preventative health. Pharmacist owned and operated. Brightpath Rovers, PLLC was started by local, Washington state licensed pharmacist with over 15 years experience vaccinating patients. She is a highly skilled immunizer and enjoys interacting with patients while providing this important preventative health services. Her vaccination experience spans from individual patient vaccinations to large clinics during community outbreaks.</p>
  <a class="btn-more">Read More</a>
</section>

<footer class="abs footer">
  <div class="brand"><i></i>Brightpath Rovers</div>
  <nav class="abs fnav">
    <a>Home</a><span class="sep">|</span><a>Aboute</a><span class="sep">|</span><a>Services</a><span class="sep">|</span><a>Schedule Today</a><span class="sep">|</span><a>Pricing</a>
  </nav>
  <div class="abs copy">Copyright © 2022 <span>Brightpath Rovers, PLLC</span>. All Rights Reserved.</div>
  <div class="abs social"><i></i><i></i><i></i></div>
</footer>

</body>
</html>
```